Stationary Set Rebrand for Brenvik

We are a Canadian Distribution and Service Company that was established in 1969. Over the past 5 decades we have expanded our business and have warehouses across Canada. We specialize in adhesive tapes, adhesives, films, safety, warehouse, shipping, janitorial and packaging supplies.

We have updated our logo design and would like a new corporate branding identity that includes a new fresh Stationary Set (Business Cards, Letterhead, Letterhead MS Word, Envelope, Presentation Folders, Email Signatures, Notepad Covers, etc.)

Target Market(s)

Industrial Business Sector

Font styles to use
Sans Serif

Colors
0054AA
0677BA
7BADD7
CADEEF
E8F1F8
0094D4
00A9DD
6FCCEA
C7EBF8
E9F6FB
00AB8E
00BBA5
67D7C9
C6EFE9
E9F9F6
EB3D1F
EC4F4E
F09395
F8D3D4
FCEDEE

Requirements
Should not have
• Colors not too light, darker colours preferred

```html
<!DOCTYPE html>
<html lang="en">
<head>
<meta charset="utf-8">
<title>Brenvik Stationery Set</title>
<link rel="stylesheet" href="https://fonts.googleapis.com/css2?family=Montserrat:wght@400;500;600;700;800&display=swap">
<style>
  :root{
    --brand-red:#d61920;
    --ink:#1b1b1b;
    --text:#555;
    --paper:#ffffff;
    --backdrop:#d3d4d6;
    --faint:#efeff0;
  }
  *{box-sizing:border-box;margin:0;padding:0}
  html,body{width:1200px;height:1008px;overflow:hidden;background:var(--backdrop)}
  body{position:relative;font-family:"Montserrat",sans-serif;color:var(--ink)}
  .sheet{position:absolute;background:var(--paper);overflow:hidden}
  .abs{position:absolute}
  .wordmark{font-family:"Montserrat",sans-serif;font-weight:800;color:var(--ink);line-height:1;letter-spacing:-.02em;white-space:nowrap}
  .wordmark.on-red{color:var(--paper)}
  .faint-disc{position:absolute;border-radius:50%;background:var(--faint)}
  .rule{position:absolute;height:1px;background:var(--ink)}
  .person{font-weight:600;line-height:1.15;white-space:nowrap}
  .person .surname{color:var(--brand-red);font-weight:700}
  .role{color:var(--text);font-weight:400}
  .contact-list{position:absolute;list-style:none;color:var(--text)}
  .contact-list li{display:flex;align-items:flex-start;gap:.5em;line-height:1.2;white-space:nowrap}
  .contact-list svg{flex:none;fill:var(--brand-red)}
  .contact-list.dark-icons svg{fill:var(--ink)}
  .contact-list.on-red{color:var(--paper)}
  .contact-list.on-red svg{fill:var(--paper)}

  /* business card front */
  .card-front{left:109px;top:105px;width:249px;height:150px}
  .card-front .wordmark{left:17px;top:18px;font-size:22px}
  .card-front .person{right:17px;top:19px;font-size:7.6px;text-align:right}
  .card-front .role{font-size:6.2px}
  .card-front .name-rule{right:17px;top:36px;width:21px;height:1px;background:var(--text)}
  .card-front .contact-list{left:17px;top:81px;font-size:5.4px}
  .card-front .contact-list li{margin-bottom:4px}
  .card-front .contact-list svg{width:7px;height:7px}
  .card-front .faint-disc{left:140px;top:60px;width:92px;height:92px}
  .card-front .rule{left:0;top:136px;width:177px}

  /* business card back */
  .card-back{left:109px;top:298px;width:249px;height:150px}
  .card-back .tab{position:absolute;top:40px;width:15px;height:70px;background:var(--brand-red)}
  .card-back .tab.left{left:0;border-radius:0 3px 3px 0}
  .card-back .tab.right{right:0;border-radius:3px 0 0 3px}
  .card-back .wordmark{left:0;right:0;top:58px;text-align:center;font-size:34px}

  /* letterhead */
  .letterhead{left:408px;top:72px;width:299px;height:419px}
  .letterhead .wordmark{left:28px;top:23px;font-size:20px}
  .letterhead .head-contacts{left:221px;top:19px;font-size:4.2px}
  .letterhead .head-contacts li{margin-bottom:3px}
  .letterhead .head-contacts svg{width:5.5px;height:5.5px}
  .recipient{position:absolute;left:28px;top:84px;font-size:5.4px;color:var(--text)}
  .recipient .to{font-size:5px}
  .recipient .recipient-name{font-size:8.2px;font-weight:700;color:var(--ink);margin:1px 0 5px}
  .recipient p{line-height:1.35}
  .recipient b{color:var(--brand-red);font-weight:700}
  .recipient .indent{padding-left:8px}
  .letter-date{position:absolute;right:24px;top:144px;font-size:5.6px;color:var(--text)}
  .letter-body{position:absolute;left:28px;top:160px;width:247px;font-size:5.85px;line-height:9.6px;color:var(--text);text-align:justify}
  .letter-body p{margin-bottom:9.6px}
  .sign-off{position:absolute;left:28px;top:326px;font-size:6.6px;font-weight:500}
  .signature-area{position:absolute;left:42px;top:338px;width:46px;height:30px;background:linear-gradient(90deg,#f4f4f4,#e9e9e9);border-radius:2px}
  .letterhead .faint-disc{left:208px;top:330px;width:84px;height:84px}
  .letterhead .rule{left:5px;top:403px;width:234px}
  .letterhead .corner-mark{position:absolute;left:0;top:399px;width:5px;height:4px;background:var(--ink)}

  /* email signature */
  .email-signature{left:747px;top:86px;width:355px;height:90px}
  .email-signature .wordmark{left:20px;top:36px;font-size:17px}
  .email-signature .person{left:98px;top:15px;font-size:6.2px}
  .email-signature .role{font-size:5.4px}
  .email-signature .name-rule{position:absolute;left:98px;top:29px;width:17px;height:1px;background:var(--text)}
  .email-signature .contact-list{left:98px;top:34px;font-size:4.3px}
  .email-signature .contact-list li{margin-bottom:3px}
  .email-signature .contact-list svg{width:5.5px;height:5.5px}
  .email-signature .faint-disc{left:178px;top:18px;width:72px;height:72px}
  .email-signature .rule{left:0;top:82px;width:206px}

  /* notepad cover */
  .notepad-cover{left:779px;top:218px;width:309px;height:438px;background:var(--brand-red)}
  .notepad-cover .cover-url{position:absolute;left:0;right:0;top:28px;text-align:center;color:var(--paper);font-size:6px;letter-spacing:.22em}
  .notepad-cover .cover-disc{position:absolute;left:18px;top:135px;width:290px;height:290px;border-radius:50%;background:var(--paper);box-shadow:0 0 0 6px #c8151c}
  .notepad-cover .wordmark{left:18px;width:290px;top:260px;text-align:center;font-size:42px}
  .binding{position:absolute;left:769px;top:228px;width:10px;height:418px;
    background:repeating-linear-gradient(180deg,transparent 0 6px,#8a8b8d 6px 9px,transparent 9px 21px)}

  /* presentation folder */
  .folder-flaps{position:absolute;left:0;top:0}
  .folder-red{left:180px;top:529px;width:263px;height:350px;background:var(--brand-red)}
  .folder-red .wordmark{left:71px;top:281px;font-size:12px}
  .folder-red .contact-list{left:129px;top:270px;font-size:4.4px}
  .folder-red .contact-list li{margin-bottom:3.4px}
  .folder-red .contact-list svg{width:5.5px;height:5.5px}
  .folder-front{left:443px;top:529px;width:263px;height:350px}
  .folder-front .wordmark{left:0;right:0;top:152px;text-align:center;font-size:34px}
  .folder-front .disc-top{left:25px;top:-20px;width:70px;height:70px}
  .folder-front .disc-bottom{left:120px;top:237px;width:126px;height:126px}

  /* envelope */
  .envelope{left:762px;top:699px;width:351px;height:177px}
  .envelope .wordmark{left:13px;top:15px;font-size:17px}
  .envelope .red-disc{position:absolute;left:193px;top:22px;width:150px;height:150px;border-radius:50%;background:var(--brand-red)}
  .envelope .window{position:absolute;left:231px;top:106px;width:89px;height:36px;border-radius:4px;background:linear-gradient(160deg,#f2f2f2,#d7d8da);border:1px solid #c9c9cb}
  .envelope .contact-list{left:14px;top:153px;font-size:4.4px}
  .envelope .contact-list svg{width:5.5px;height:5.5px}
  .envelope .rule{left:0;top:162px;width:253px}
</style>
</head>
<body>

<svg width="0" height="0" style="position:absolute" aria-hidden="true">
  <symbol id="icon-pin" viewBox="0 0 10 10"><rect width="10" height="10" rx="1.5"/><path d="M5 2a2 2 0 0 1 2 2c0 1.5-2 4-2 4S3 5.5 3 4a2 2 0 0 1 2-2z" fill="#fff"/></symbol>
  <symbol id="icon-phone" viewBox="0 0 10 10"><rect width="10" height="10" rx="1.5"/><path d="M3 2.2l1.2 1.4-.6.8c.4.9 1 1.5 1.9 1.9l.8-.6L7.8 7 7 8c-2.6-.3-4.7-2.4-5-5z" fill="#fff"/></symbol>
  <symbol id="icon-mail" viewBox="0 0 10 10"><rect width="10" height="10" rx="1.5"/><path d="M2 3h6v4H2z" fill="#fff"/><path d="M2 3l3 2.2L8 3" fill="none" stroke="currentColor" stroke-width=".6"/></symbol>
  <symbol id="icon-cursor" viewBox="0 0 10 10"><rect width="10" height="10" rx="1.5"/><path d="M3 2l4.5 3.5-2 .3 1.2 2.2-.8.4-1.2-2.2L3.2 7.5z" fill="#fff"/></symbol>
</svg>

<!-- Business card front -->
<section class="sheet card-front" aria-label="Business card front">
  <div class="faint-disc" aria-hidden="true"></div>
  <div class="abs wordmark">Brenvik</div>
  <div class="abs person">DANIEL R. <span class="surname">HARTLEY</span><br><span class="role">Managing Director</span></div>
  <div class="abs name-rule"></div>
  <ul class="contact-list dark-icons">
    <li><svg><use href="#icon-pin"/></svg><span>2750 Harbour Road<br>Halifax, NS B3K 0A1</span></li>
    <li><svg style="fill:var(--brand-red)"><use href="#icon-phone"/></svg><span>+1 902 555 0148</span></li>
    <li><svg style="fill:var(--brand-red)"><use href="#icon-mail"/></svg><span>hello@brenvik.ca</span></li>
    <li><svg style="fill:var(--brand-red)"><use href="#icon-cursor"/></svg><span>www.brenvik.ca</span></li>
  </ul>
  <div class="rule"></div>
</section>

<!-- Business card back -->
<section class="sheet card-back" aria-label="Business card back">
  <div class="tab left"></div>
  <div class="abs wordmark">Brenvik</div>
  <div class="tab right"></div>
</section>

<!-- Letterhead -->
<section class="sheet letterhead" aria-label="Letterhead">
  <div class="abs wordmark">Brenvik</div>
  <ul class="contact-list head-contacts">
    <li><svg><use href="#icon-pin"/></svg><span>2750 Harbour Road<br>Halifax, NS B3K 0A1</span></li>
    <li><svg><use href="#icon-phone"/></svg><span>+1 902 555 0148</span></li>
    <li><svg><use href="#icon-mail"/></svg><span>hello@brenvik.ca</span></li>
    <li><svg><use href="#icon-cursor"/></svg><span>www.brenvik.ca</span></li>
  </ul>
  <div class="recipient">
    <div class="to">To</div>
    <div class="recipient-name">MARA OLSEN</div>
    <p><b>A :</b> 88 Cedar Lane, Suite 40<br><span class="indent">Moncton, NB E1C 4H2</span></p>
    <p style="margin-top:3px"><b>P :</b> 506-555-0172</p>
    <p style="margin-top:2px"><b>E :</b> m.olsen@northmail.ca</p>
  </div>
  <div class="letter-date">12 December, 2024</div>
  <div class="letter-body">
    <p>Lorem ipsum dolor sit amet, consectetuer adipiscing elit, sed diam nonummy nibh euismod tincidunt ut laoreet dolore magna aliquam erat volutpat. Ut wisi enim ad minim veniam, quis nostrud exerci tation ullamcorper suscipit lobortis nisl ut aliquip ex ea commodo consequat. Duis autem vel eum iriure dolor in hendrerit in vulputate velit esse molestie consequat, vel illum dolore eu feugiat nulla facilisis at vero eros et accumsan et iusto odio dignissim qui blandit praesent luptatum zzril delenit augue duis dolore te feugait nulla facilisi.</p>
    <p>Lorem ipsum dolor sit amet, cons ectetuer adipiscing elit, sed diam nonummy nibh euismod tincidunt ut laoreet dolore magna aliquam erat volutpat. Ut wisi enim ad minim veniam, quis nostrud exerci tation ullamcorper suscipit lobortis nisl ut aliquip ex ea commodo consequat.</p>
    <p>Lorem ipsum dolor sit amet, consectetuer adipiscing elit, sed diam nonummy nibh euismod tincidunt ut laoreet dolore magna aliquam erat</p>
  </div>
  <div class="sign-off">Mr. Daniel R. Hartley</div>
  <div class="signature-area" role="img" aria-label="Handwritten signature of the sender"></div>
  <div class="faint-disc" aria-hidden="true"></div>
  <div class="corner-mark"></div>
  <div class="rule"></div>
</section>

<!-- Email signature -->
<section class="sheet email-signature" aria-label="Email signature">
  <div class="faint-disc" aria-hidden="true"></div>
  <div class="abs wordmark">Brenvik</div>
  <div class="abs person">DANIEL R. <span class="surname">HARTLEY</span><br><span class="role">Managing Director</span></div>
  <div class="name-rule"></div>
  <ul class="contact-list">
    <li><svg style="fill:var(--ink)"><use href="#icon-pin"/></svg><span>2750 Harbour Road<br>Halifax, NS B3K 0A1</span></li>
    <li><svg><use href="#icon-phone"/></svg><span>+1 902 555 0148</span></li>
    <li><svg><use href="#icon-mail"/></svg><span>hello@brenvik.ca</span></li>
    <li><svg><use href="#icon-cursor"/></svg><span>www.brenvik.ca</span></li>
  </ul>
  <div class="rule"></div>
</section>

<!-- Notepad cover -->
<div class="binding" aria-hidden="true"></div>
<section class="sheet notepad-cover" aria-label="Notepad cover">
  <div class="cover-url">www.brenvik.ca</div>
  <div class="cover-disc" aria-hidden="true"></div>
  <div class="abs wordmark">Brenvik</div>
</section>

<!-- Presentation folder -->
<svg class="folder-flaps" width="1200" height="1008" aria-hidden="true">
  <path d="M180 529 L110 542 Q93 546 93 565 L93 842 Q93 861 110 865 L180 879 Z" fill="#ffffff"/>
  <path d="M180 879 L193 942 Q198 966 222 966 L400 966 Q424 966 429 942 L443 879 Z" fill="#ffffff"/>
</svg>
<section class="sheet folder-red" aria-label="Presentation folder back panel">
  <div class="abs wordmark on-red">Brenvik</div>
  <ul class="contact-list on-red">
    <li><svg><use href="#icon-pin"/></svg><span>2750 Harbour Road<br>Halifax, NS B3K 0A1</span></li>
    <li><svg><use href="#icon-phone"/></svg><span>+1 902 555 0148</span></li>
    <li><svg><use href="#icon-mail"/></svg><span>hello@brenvik.ca</span></li>
    <li><svg><use href="#icon-cursor"/></svg><span>www.brenvik.ca</span></li>
  </ul>
</section>
<section class="sheet folder-front" aria-label="Presentation folder front panel">
  <div class="faint-disc disc-top" aria-hidden="true"></div>
  <div class="faint-disc disc-bottom" aria-hidden="true"></div>
  <div class="abs wordmark">Brenvik</div>
</section>

<!-- Envelope -->
<section class="sheet envelope" aria-label="Envelope">
  <div class="abs wordmark">Brenvik</div>
  <div class="red-disc" aria-hidden="true"></div>
  <div class="window" aria-hidden="true"></div>
  <ul class="contact-list">
    <li><svg><use href="#icon-pin"/></svg><span>2750 Harbour Road Halifax, NS B3K 0A1</span></li>
  </ul>
  <div class="rule"></div>
</section>

</body>
</html>
```